T's Gluten Free Bakery Cookie Package

What: We need a bag design for a gluten free cookie. <br/>Product: Sugar Cookie<br/>Background: T's Gluten Free is a family owned company that was started by a mom doing a favor for her daughter. The founder, Tolva (T's), made gluten free bread for her daughter's friend with Celiac disease. She wanted to keep doing it for others because it gave her so much happiness to see people enjoy food that they thought they'd never eat again. These cookies are made with a mother's love!<br/>Bag info: Our bag is green with a small round window to see the cookie. 4.25" W x 8.5" H. The nutritional label will go on the back.<br/>Bag design: Definitely include the medallion shape with the E inside of it. Put the product name on the bag (Sugar Cookie)<br/>
People with Celiac disease. People who are living/eating healthy and want gluten free that tastes good. They're willing to pay more quality item.

```html
<!DOCTYPE html>
<html lang="en">
<head>
<meta charset="utf-8">
<title>T's Gluten Free Bakery – Lemon Sugar Cookie Bag</title>
<link rel="stylesheet" href="https://fonts.googleapis.com/css2?family=Roboto+Slab:wght@400;700;800&family=Arvo&family=Allura&family=Fjalla+One&family=Open+Sans&family=Roboto:wght@400;700&display=swap">
<style>
  :root {
    --lime: #d7e037;
    --purple: #46306b;
    --white: #ffffff;
    --page: #ffffff;
    --cookie-dark: #8a5a33;
    --cookie-light: #b98456;
    --photo-dark: #2e2e2e;
    --photo-light: #9a9a9a;
  }
  * { box-sizing: border-box; margin: 0; padding: 0; }
  html, body { width: 1200px; height: 1144px; overflow: hidden; background: var(--page); }
  .canvas { position: relative; width: 1200px; height: 1144px; }

  .panel {
    position: absolute; top: 17px; width: 558px; height: 1114px;
    background: var(--lime); border-radius: 38px; overflow: hidden; color: var(--purple);
  }
  .panel--front { left: 13px; }
  .panel--back { left: 633px; }
  .panel__swoop { position: absolute; inset: 0; width: 558px; height: 1114px; }
  .panel__swoop path { fill: var(--purple); }

  /* Front */
  .brand { position: absolute; left: 0; width: 470px; top: 182px; text-align: center; }
  .brand__ring {
    width: 190px; height: 190px; margin: 0 auto; border: 9px solid var(--purple); border-radius: 50%;
  }
  .brand__name {
    margin-top: 18px; font-family: "Roboto Slab", serif; font-weight: 800;
    font-size: 44px; line-height: 46px; color: var(--purple);
  }
  .product { position: absolute; left: 176px; top: 558px; width: 260px; z-index: 1; }
  .product__flavour {
    font-family: "Arvo", serif; font-size: 27px; line-height: 32px; color: var(--purple);
    padding-left: 34px; white-space: nowrap;
  }
  .product__type {
    font-family: "Allura", cursive; font-size: 80px; line-height: 66px; color: var(--purple);
    white-space: nowrap;
    text-shadow: 1px 0 0 var(--white), -1px 0 0 var(--white), 0 1px 0 var(--white), 0 -1px 0 var(--white),
                 1px 1px 0 var(--white), -1px -1px 0 var(--white), 1px -1px 0 var(--white), -1px 1px 0 var(--white);
  }
  .cookie-art {
    position: absolute; left: 125px; top: 729px; width: 263px; height: 207px; border-radius: 48%;
    background: radial-gradient(circle at 40% 40%, var(--cookie-light), var(--cookie-dark));
  }
  .tagline { position: absolute; left: 41px; top: 1010px; font-family: "Arvo", serif; color: var(--purple); }
  .tagline__lead { font-size: 20px; line-height: 24px; }
  .tagline__punch { font-size: 27px; line-height: 30px; }
  .net-weight {
    position: absolute; left: 461px; top: 1045px; font-family: "Roboto", sans-serif;
    font-weight: 700; font-size: 19px; color: var(--white);
  }

  /* Back */
  .ingredients {
    position: absolute; left: 51px; top: 190px; width: 440px;
    font-family: "Fjalla One", sans-serif; font-size: 19px; line-height: 25.5px; color: var(--purple);
  }
  .ingredients__note { margin-top: 25px; }

  .nutrition {
    position: absolute; left: 46px; top: 430px; width: 259px; height: 431px;
    background: var(--white); border: 2px solid #cfcfcf; padding: 9px 10px 6px 14px;
    font-family: "Roboto", sans-serif; color: var(--purple); font-size: 10px;
  }
  .nutrition__title { font-size: 18px; font-weight: 700; border-bottom: 1px solid var(--purple); padding-bottom: 1px; }
  .nutrition__row { display: flex; justify-content: space-between; padding: 2px 0; }
  .nutrition__row--bold { font-size: 11px; }
  .nutrition__row--bold > span:first-child { font-weight: 700; }
  .nutrition__row--sub { padding-left: 14px; }
  .nutrition__row--subsub { padding-left: 26px; }
  .nutrition__rule { border-bottom: 1px solid var(--purple); }
  .nutrition__rule--thick { border-bottom: 3px solid var(--purple); }
  .nutrition__row--tall { padding: 8px 0 7px; }
  .nutrition__dv { text-align: right; font-size: 7px; padding: 1px 10px 2px 0; }
  .nutrition__foot { font-size: 6.5px; line-height: 8px; margin-top: 12px; }

  .founder-photo {
    position: absolute; left: 353px; top: 427px; width: 138px; height: 126px;
    background: linear-gradient(160deg, var(--photo-light), var(--photo-dark));
  }
  .story {
    position: absolute; left: 323px; top: 558px; width: 218px;
    font-family: "Open Sans", sans-serif; font-size: 19px; line-height: 24.7px; color: var(--purple);
  }
  .social { position: absolute; left: 60px; top: 994px; font-family: "Open Sans", sans-serif; font-size: 17px; color: var(--purple); }
  .social__item { display: flex; align-items: center; gap: 6px; line-height: 24px; }
  .social__dot { width: 14px; height: 14px; border-radius: 50%; background: var(--purple); }
  .website {
    position: absolute; left: 340px; top: 1042px; font-family: "Open Sans", sans-serif;
    font-size: 17px; color: var(--white);
  }
</style>
</head>
<body>
<main class="canvas">

  <section class="panel panel--front" aria-label="Bag front">
    <svg class="panel__swoop" viewBox="0 0 558 1114" aria-hidden="true">
      <path d="M444 0 C490 90 505 180 480 290 C445 440 370 620 330 800 C300 940 285 1020 295 1114 L558 1114 L558 0 Z"/>
    </svg>
    <div class="brand">
      <div class="brand__ring" aria-hidden="true"></div>
      <p class="brand__name">T's Gluten Free<br>Bakery</p>
    </div>
    <div class="product">
      <p class="product__flavour">Lemon Sugar</p>
      <p class="product__type">Cookie</p>
    </div>
    <div class="cookie-art" role="img" aria-label="Illustration of two cookies"></div>
    <div class="tagline">
      <p class="tagline__lead">If it tastes gluten free,</p>
      <p class="tagline__punch">then it's not T's</p>
    </div>
    <p class="net-weight">6 oz</p>
  </section>

  <section class="panel panel--back" aria-label="Bag back">
    <svg class="panel__swoop" viewBox="0 0 558 1114" aria-hidden="true">
      <path d="M0 1075 C120 1115 250 1090 360 1020 C440 970 500 945 558 952 L558 1114 L0 1114 Z"/>
    </svg>
    <div class="ingredients">
      <p>Ingredients:</p>
      <p>TGF flour (brown rice, white rice, sweet rice, tapioca starch), xanthan, citric acid, lemon peel, baking soda,baking powder, salt, sugar, cream cheese, butter, vegetable oil, eggs, milk, vanilla extract, lemon extract.</p>
      <p>❖Contains milk and eggs❖</p>
      <p class="ingredients__note">Proprietary flour mix is free of soy and cornstarch</p>
    </div>

    <div class="nutrition" aria-label="Nutrition Facts">
      <p class="nutrition__title">Nutrition Facts</p>
      <p class="nutrition__row">6 serving per container</p>
      <p class="nutrition__row nutrition__row--bold nutrition__rule--thick" style="font-weight:700"><span>Serving Size</span><span>1 oz (28)</span></p>
      <p class="nutrition__row" style="padding-top:5px">Amount per serving</p>
      <p class="nutrition__row nutrition__row--bold nutrition__rule" style="padding-top:0;font-weight:700"><span>Calories</span><span>120</span></p>
      <p class="nutrition__dv nutrition__rule">% Daily Value*</p>
      <p class="nutrition__row nutrition__row--bold" style="padding-top:6px"><span>Total Fat 4.5g</span><span>6%</span></p>
      <p class="nutrition__row nutrition__row--sub nutrition__rule"><span>Saturated Fat 2g</span><span>10%</span></p>
      <p class="nutrition__row nutrition__row--sub nutrition__rule">Trans Fat 0g</p>
      <p class="nutrition__row nutrition__row--bold nutrition__row--tall nutrition__rule"><span>Cholesterol 10mg</span><span>3 %</span></p>
      <p class="nutrition__row nutrition__row--bold nutrition__row--tall nutrition__rule"><span>Sodium 25mg</span><span>1%</span></p>
      <p class="nutrition__row nutrition__row--bold" style="padding-top:6px"><span>Total Carbohydrates 18g</span><span>7%</span></p>
      <p class="nutrition__row nutrition__row--sub nutrition__rule"><span>Dietary Fiber 0g</span><span>0%</span></p>
      <p class="nutrition__row nutrition__row--sub nutrition__rule">Total Sugars 9g</p>
      <p class="nutrition__row nutrition__row--subsub"><span>includes 9g Added Sugars</span><span>0%</span></p>
      <p class="nutrition__row nutrition__row--bold nutrition__rule--thick" style="padding:4px 0 6px"><span>Protein 1g</span></p>
      <p class="nutrition__row" style="padding-left:8px;padding-top:5px"><span>Vitamin D 0mcg</span><span>0%</span></p>
      <p class="nutrition__row nutrition__rule" style="padding-left:8px"><span>Calcium 4mg</span><span>0%</span></p>
      <p class="nutrition__row nutrition__rule" style="padding-left:8px"><span>Iron 0mg</span><span>0%</span></p>
      <p class="nutrition__row nutrition__rule--thick" style="padding-left:8px;font-size:11px"><span>Potassium 18mg</span><span>0%</span></p>
      <p class="nutrition__foot">* The % Daily Value tells you how much a nutrient in a serving of food contributes to a daily diet. 2,000 calories a day is used for general nutrition advice.</p>
    </div>

    <div class="founder-photo" role="img" aria-label="Black and white portrait of the founder, Tolva"></div>
    <p class="story">My passion for baking was sparked at the age of nine when I baked my first cake in a wood burning stove. Years later, I made my first loaf of gluten free bread for my daughter's friend and realized I had a knack for making gluten free, not taste gluten free. I know you will enjoy my homemade, additive-free, gluten-free baked goods.</p>

    <div class="social">
      <p class="social__item"><span class="social__dot" aria-hidden="true"></span>tsbakeshop</p>
      <p class="social__item"><span class="social__dot" aria-hidden="true"></span>tsbakeshop</p>
    </div>
    <p class="website">www.tsbakeshop-gf.com</p>
  </section>

</main>
</body>
</html>
```